KPL Business Card Design

I am attaching my logo and want both a black and white modern, contemporary card for my business.

Below are the details I require on the cards and of course I would need to be able to change this.

Thanks

Rob

Robert J Harcourt

Sales & Marketing Director

 

Vivid Panel Gazette

PO Box 4417

Chatham

Kent

ME7 5QX

 

Tel +44 (0) 1632 960 418

Mobile: +44 (0) 7700 900 537

Fax: +44 (0) 1632 960 772

Email: rob@vividpanelgazette.example

Website: www.vividpanelgazette.example

 

 

Be part of a World full of imagination,

knowledge and inspiration

 

 

Derek Pashley

Editorial Director

 

Vivid Panel Gazette

42 Fernhurst Close

Whitton

Middlesex

TW7 4LN

 

Tel: +44 (0) 208 496 0213

Mobile: +44 (0) 7700 900 864

Email: derek@vividpanelgazette.example

 

 

knowledge and inspiration

This is the same font as used in the logo.......

Robert J Harcourt

 

Vivid Panel Gazette

PO Box 4417

Chatham

Kent

ME7 5QX

 

Tel +44 (0) 1632 960 418

Fax: +44 (0) 1632 960 772

 

 

Derek Pashley

Editorial Director

 

Vivid Panel Gazette

42 Fernhurst Close

Whitton

Middlesex

TW7 4LN

 

Tel: +44 (0) 208 496 0213

Please add the following words to the back of the card and maybe add the logo to the back again.....

knowledge and inspiration

Robert J Harcourt

 

Vivid Panel Gazette

PO Box 4417

Chatham

Kent

ME7 5QX

 

Tel +44 (0) 1632 960 418

Fax: +44 (0) 1632 960 772

 

 

Derek Pashley

Editorial Director

 

Vivid Panel Gazette

42 Fernhurst Close

Whitton

Middlesex

TW7 4LN

 

Tel: +44 (0) 208 496 0213

knowledge and inspiration

Target Market(s)

Wide Format printing, Screen Printing, Digital Printing, Textile Printing, Signage, Digital Signage, Exhibition Graphics, Digital Textiles and more

Industry/Entity Type

Publishing

Requirements
Must have
• I would like to use these words on the back of the card both for a full black card and white card.

"Be part of a World full of imagination, knowledge and inspiration"

```html
<!DOCTYPE html>
<html lang="en">
<head>
<meta charset="utf-8">
<title>Vivid Panel Gazette – Business Card Concepts</title>
<link href="https://fonts.googleapis.com/css2?family=Gelasio:wght@400;700&family=Pinyon+Script&display=swap" rel="stylesheet">
<style>
  :root {
    --ink: #111111;
    --paper: #ffffff;
    --night: #000000;
    --orange: #f7941d;
    --grey: #8f8f8f;
    --soft: rgba(140, 150, 170, 0.16);
    --soft-dark: rgba(255, 255, 255, 0.12);
    --card-w: 294px;
    --card-h: 164px;
  }
  * { box-sizing: border-box; margin: 0; padding: 0; }
  html, body { width: 1200px; height: 657px; overflow: hidden; background: var(--paper); }
  body { position: relative; font-family: "Gelasio", Georgia, serif; color: var(--ink); }

  .night-band { position: absolute; left: 0; top: 0; width: 1176px; height: 164px; background: var(--night); }

  .card { position: absolute; width: var(--card-w); height: var(--card-h); overflow: hidden; }
  .card.is-color { --accent: var(--orange); }
  .card.is-mono { --accent: var(--grey); }
  .card.is-dark { color: var(--paper); }
  .card.is-dark.is-mono { --accent: var(--paper); }

  .col-1 { left: 0; } .col-2 { left: 294px; } .col-3 { left: 588px; } .col-4 { left: 882px; }
  .row-1 { top: 0; } .row-2 { top: 173px; } .row-3 { top: 329px; } .row-4 { top: 496px; }

  .brand { position: absolute; display: flex; align-items: center; gap: 6px; }
  .brand-dot { width: 34px; height: 34px; border-radius: 50%; background: var(--accent); flex: none; }
  .brand-name { font-weight: 700; font-size: 15px; color: var(--accent); white-space: nowrap; line-height: 1; }
  .brand.is-large .brand-name { font-size: 19px; }

  .decor { position: absolute; border-radius: 50%; background: var(--soft); }
  .is-dark .decor { background: var(--soft-dark); }

  .person { position: absolute; line-height: 1.15; }
  .person-name { font-weight: 700; font-size: 13px; }
  .person-role { font-size: 10px; }
  .is-color .person-name.is-accent { color: var(--accent); }

  .contacts { position: absolute; font-size: 7.6px; line-height: 1.3; }
  .contacts .tel { font-weight: 700; font-size: 8.6px; }
  .align-right { text-align: right; }
  .align-center { text-align: center; }
  .org { font-weight: 700; color: var(--accent); }

  .panel { position: absolute; left: 0; top: 0; width: 164px; height: 110px; padding: 12px 10px; }
  .is-color .panel { background: var(--orange); color: var(--ink); }
  .is-mono .panel { background: var(--night); color: var(--paper); }
  .panel .person-name { font-size: 16px; }
  .panel .person-role { font-size: 13px; margin-bottom: 8px; }
  .panel .contacts { position: static; font-size: 8.4px; }
  .panel .contacts .tel { font-size: 9.4px; }

  .slogan {
    position: absolute; left: 0; top: 0; width: 100%; height: 100%;
    display: flex; flex-direction: column; justify-content: center; padding-left: 22px;
    font-family: "Pinyon Script", cursive; font-size: 21px; line-height: 1.32; font-weight: 400;
  }
  .slogan span:nth-child(1) { padding-left: 14px; }
  .slogan span:nth-child(2) { padding-left: 34px; }
</style>
</head>
<body>
  <div class="night-band"></div>

  <!-- Row 1: black cards -->
  <section class="card is-dark is-color col-1 row-1">
    <div class="brand" style="left:10px;top:24px"><span class="brand-dot"></span><span class="brand-name">Vivid Panel Gazette</span></div>
    <div class="person align-right" style="right:12px;top:80px">
      <p class="person-name is-accent">Robert J Harcourt</p>
      <p class="person-role">Sales &amp; Marketing Director</p>
    </div>
    <div class="contacts" style="left:12px;top:115px">
      <p class="org">Vivid Panel Gazette</p>
      <p>PO Box 4417, Chatham, Kent, ME7 5QX</p>
      <p>Email: rob@vividpanelgazette.example</p>
      <p>Website: www.vividpanelgazette.example</p>
    </div>
    <div class="contacts align-right" style="right:12px;top:125px">
      <p class="tel">Tel +44 (0) 1632 960 418</p>
      <p>Mobile: +44 (0) 7700 900 537</p>
      <p>Fax: +44 (0) 1632 960 772</p>
    </div>
  </section>

  <section class="card is-dark is-color col-2 row-1">
    <div class="decor" style="left:200px;top:10px;width:120px;height:120px"></div>
    <p class="slogan"><span>Be part of a World full</span><span>of imagination,</span><span>knowledge and inspiration</span></p>
  </section>

  <section class="card is-dark is-mono col-3 row-1">
    <div class="decor" style="left:150px;top:10px;width:130px;height:130px"></div>
    <div class="brand" style="left:10px;top:24px"><span class="brand-dot"></span><span class="brand-name">Vivid Panel Gazette</span></div>
    <div class="person" style="left:12px;top:92px">
      <p class="person-name">Robert J Harcourt</p>
      <p class="person-role">Sales &amp; Marketing Director</p>
    </div>
    <div class="contacts" style="left:12px;top:128px">
      <p>PO Box 4417, Chatham, Kent, ME7 5QX</p>
      <p>Email: rob@vividpanelgazette.example</p>
      <p>Website: www.vividpanelgazette.example</p>
    </div>
    <div class="contacts align-right" style="right:8px;top:128px">
      <p class="tel">Tel +44 (0) 1632 960 418</p>
      <p>Mobile: +44 (0) 7700 900 537</p>
      <p>Fax: +44 (0) 1632 960 772</p>
    </div>
  </section>

  <section class="card is-dark is-mono col-4 row-1">
    <div class="decor" style="left:200px;top:10px;width:120px;height:120px"></div>
    <p class="slogan"><span>Be part of a World full</span><span>of imagination,</span><span>knowledge and inspiration</span></p>
  </section>

  <!-- Row 2: white cards, top-left brand -->
  <section class="card is-color col-1 row-2">
    <div class="decor" style="left:180px;top:20px;width:130px;height:150px"></div>
    <div class="brand" style="left:10px;top:8px"><span class="brand-dot"></span><span class="brand-name" style="font-size:12px">Vivid Panel<br>Gazette</span></div>
    <div class="person align-right" style="right:10px;top:13px">
      <p class="person-name">Derek Pashley</p>
      <p class="person-role">Editorial Director</p>
    </div>
    <div class="contacts align-right" style="right:10px;top:47px">
      <p class="tel">Tel +44 (0) 208 496 0213</p>
      <p>Mobile: +44 (0) 7700 900 864</p>
      <p>Fax: +44 (0) 1632 960 772</p>
    </div>
    <div class="contacts" style="left:8px;top:115px">
      <p>42 Fernhurst Close, Whitton, Middlesex, TW7 4LN</p>
      <p>Email: derek@vividpanelgazette.example</p>
      <p>Website: www.vividpanelgazette.example</p>
    </div>
  </section>

  <section class="card is-color col-2 row-2">
    <div class="decor" style="left:120px;top:25px;width:140px;height:140px"></div>
    <p class="slogan"><span>Be part of a World full</span><span>of imagination,</span><span>knowledge and inspiration</span></p>
  </section>

  <section class="card is-mono col-3 row-2">
    <div class="decor" style="left:180px;top:20px;width:130px;height:150px"></div>
    <div class="brand" style="left:10px;top:8px"><span class="brand-dot"></span><span class="brand-name" style="font-size:12px;color:var(--ink)">Vivid Panel<br>Gazette</span></div>
    <div class="person align-right" style="right:10px;top:13px">
      <p class="person-name">Derek Pashley</p>
      <p class="person-role">Editorial Director</p>
    </div>
    <div class="contacts align-right" style="right:10px;top:47px">
      <p class="tel">Tel +44 (0) 208 496 0213</p>
      <p>Mobile: +44 (0) 7700 900 864</p>
      <p>Fax: +44 (0) 1632 960 772</p>
    </div>
    <div class="contacts" style="left:8px;top:115px">
      <p>42 Fernhurst Close, Whitton, Middlesex, TW7 4LN</p>
      <p>Email: derek@vividpanelgazette.example</p>
      <p>Website: www.vividpanelgazette.example</p>
    </div>
  </section>

  <section class="card is-mono col-4 row-2">
    <div class="decor" style="left:120px;top:25px;width:140px;height:140px"></div>
    <p class="slogan"><span>Be part of a World full</span><span>of imagination,</span><span>knowledge and inspiration</span></p>
  </section>

  <!-- Row 3: colour block panel -->
  <section class="card is-color col-1 row-3">
    <div class="panel">
      <p class="person-name">Derek Pashley</p>
      <p class="person-role">Editorial Director</p>
      <div class="contacts">
        <p class="tel">Tel +44 (0) 208 496 0213</p>
        <p>Mobile: +44 (0) 7700 900 864</p>
        <p>Fax: +44 (0) 1632 960 772</p>
      </div>
    </div>
    <div class="brand" style="left:146px;top:42px"><span class="brand-dot"></span><span class="brand-name" style="font-size:12px">Vivid Panel<br>Gazette</span></div>
    <div class="contacts align-center" style="left:0;width:100%;top:115px;font-size:8px">
      <p>42 Fernhurst Close, Whitton, Middlesex, TW7 4LN</p>
      <p>Email: derek@vividpanelgazette.example</p>
      <p>Website: www.vividpanelgazette.example</p>
    </div>
  </section>

  <section class="card is-color col-2 row-3">
    <div class="decor" style="left:120px;top:40px;width:140px;height:140px"></div>
    <p class="slogan"><span>Be part of a World full</span><span>of imagination,</span><span>knowledge and inspiration</span></p>
  </section>

  <section class="card is-mono col-3 row-3">
    <div class="panel">
      <p class="person-name">Derek Pashley</p>
      <p class="person-role">Editorial Director</p>
      <div class="contacts">
        <p class="tel">Tel +44 (0) 208 496 0213</p>
        <p>Mobile: +44 (0) 7700 900 864</p>
        <p>Fax: +44 (0) 1632 960 772</p>
      </div>
    </div>
    <div class="brand" style="left:146px;top:42px"><span class="brand-dot"></span><span class="brand-name" style="font-size:12px;color:var(--ink)">Vivid Panel<br>Gazette</span></div>
    <div class="contacts align-center" style="left:0;width:100%;top:115px;font-size:8px">
      <p>42 Fernhurst Close, Whitton, Middlesex, TW7 4LN</p>
      <p>Email: derek@vividpanelgazette.example</p>
      <p>Website: www.vividpanelgazette.example</p>
    </div>
  </section>

  <section class="card is-mono col-4 row-3">
    <div class="decor" style="left:120px;top:40px;width:140px;height:140px"></div>
    <p class="slogan"><span>Be part of a World full</span><span>of imagination,</span><span>knowledge and inspiration</span></p>
  </section>

  <!-- Row 4: name top-left, large brand -->
  <section class="card is-color col-1 row-4">
    <div class="person" style="left:12px;top:8px">
      <p class="person-name" style="font-size:16px">Derek Pashley</p>
      <p class="person-role" style="font-size:13px">Editorial Director</p>
    </div>
    <div class="brand is-large" style="left:152px;top:6px"><span class="brand-name" style="line-height:1.05">Vivid Panel<br>Gazette</span></div>
    <div class="contacts" style="left:12px;top:58px">
      <p class="tel">Tel +44 (0) 208 496 0213</p>
      <p>Mobile: +44 (0) 7700 900 864</p>
      <p>Fax: +44 (0) 1632 960 772</p>
    </div>
    <div class="contacts" style="left:12px;top:99px;font-size:8px">
      <p>42 Fernhurst Close, Whitton, Middlesex, TW7 4LN</p>
      <p>Email: derek@vividpanelgazette.example</p>
      <p>Website: www.vividpanelgazette.example</p>
    </div>
  </section>

  <section class="card is-color col-2 row-4">
    <div class="decor" style="left:120px;top:20px;width:140px;height:140px"></div>
    <p class="slogan"><span>Be part of a World full</span><span>of imagination,</span><span>knowledge and inspiration</span></p>
  </section>

  <section class="card is-mono col-3 row-4">
    <div class="person" style="left:12px;top:8px">
      <p class="person-name" style="font-size:16px">Derek Pashley</p>
      <p class="person-role" style="font-size:13px">Editorial Director</p>
    </div>
    <div class="brand is-large" style="left:152px;top:6px"><span class="brand-name" style="line-height:1.05">Vivid Panel<br>Gazette</span></div>
    <div class="contacts" style="left:12px;top:58px">
      <p class="tel">Tel +44 (0) 208 496 0213</p>
      <p>Mobile: +44 (0) 7700 900 864</p>
      <p>Fax: +44 (0) 1632 960 772</p>
    </div>
    <div class="contacts" style="left:12px;top:99px;font-size:8px">
      <p>42 Fernhurst Close, Whitton, Middlesex, TW7 4LN</p>
      <p>Email: derek@vividpanelgazette.example</p>
      <p>Website: www.vividpanelgazette.example</p>
    </div>
  </section>

  <section class="card is-mono col-4 row-4">
    <div class="decor" style="left:120px;top:20px;width:140px;height:140px"></div>
    <p class="slogan"><span>Be part of a World full</span><span>of imagination,</span><span>knowledge and inspiration</span></p>
  </section>
</body>
</html>
```